Drug safety monitoring company requires a new corporate website

We are an outsourcing partner to large and small companies within the pharmaceutical industry. Our current website www.orbanquill.co.uk has not been updated in a long time. We want a new web site that is responsive and modern but with a clearly corporate and professional feel. We want a design based on a 12 column grid system (mobile and desktop version). We want to use a new, modern font (not the standard web fonts) - we will purchase as required. Content can be used as is from the current website. Red and white are the corporate colours, so a palate should be developed to match. We do not need as much red as is in the current website. New icons (preferably in svg format) would be great. We can also purchase new images from PhotoVane (or other) as required. We would prefer submissions in Sketch if possible.

Target Market(s)

Pharmaceutical companies

Number of Pages Required

1 page

Font styles to use
Sans Serif

Colors
ec1f27
ffffff

Requirements
Must have
• Design based on 12 column grid system.
Responsive design (i.e. require a mobile and desktop version).
How should the menu look between desktop and mobile?
A coherent colour palete.
Content to come from the existing website: www.orbanquill.co.uk
How should links be styled?
How should headings, sub-headings, paragraphs be styled?
Nice to have
• Custom developed icons (these are along the bottom of the page on the existing website: Medical Information; Pharmacovigilance; Literature Monitoring; Training).
New imagery (the images on the current website are dated).
Submission ideally as Sketch files (but we are okay with photoshop too).
A new, modern, non-standard font.
Not so much red in the design.
If we had buttons on the website, how should they be styled?
If we had a form on the website, how should the fields be styled?

```html
<!DOCTYPE html>
<html lang="en">
<head>
<meta charset="utf-8">
<title>Orban Quill Pharmacovigilance – Mobile Home</title>
<link rel="stylesheet" href="https://fonts.googleapis.com/css2?family=Rubik:wght@400;500;700&family=Lato:wght@400;700&display=swap">
<style>
  :root{
    --brand-red:#ec1f27;
    --deep-red:#c8101a;
    --menu-red:rgba(200,16,26,.92);
    --white:#ffffff;
    --ink:#3a3a3a;
    --body-ink:#4a4a4a;
    --blush:#fdf1f1;
    --stage:#eef0f2;
    --rule:#d9d9d9;
    --cream:#f3ecc8;
  }
  *{box-sizing:border-box;margin:0;padding:0}
  html,body{width:1200px;height:993px;overflow:hidden}
  body{background:var(--stage);position:relative;font-family:"Lato",sans-serif}

  .screen{position:absolute;width:372px;height:640px;background:var(--white);overflow:hidden;
    box-shadow:0 10px 30px rgba(0,0,0,.12);transform-origin:top left}
  .screen--compact{left:174px;top:275px;transform:scale(.862)}
  .screen--menu-open{left:640px;top:182px}

  .site-header{position:absolute;left:0;top:0;width:100%;height:34px;background:var(--brand-red);
    display:flex;align-items:center;padding:0 10px;font-family:"Rubik",sans-serif;color:var(--white)}
  .brand{font-size:9px;font-weight:700;letter-spacing:.08em;text-transform:uppercase;display:flex;align-items:center;gap:4px;white-space:nowrap}
  .brand-dot{width:7px;height:7px;border-radius:50%;background:var(--white)}
  .site-title{flex:1;text-align:center;font-size:9.5px;font-weight:400;color:rgba(255,255,255,.82);white-space:nowrap}
  .site-title strong{color:var(--white);font-weight:700}
  .menu-toggle{width:16px;height:16px;display:flex;flex-direction:column;justify-content:center;gap:2.5px}
  .menu-toggle span{display:block;height:1.3px;background:var(--white)}
  .screen--menu-open .menu-toggle{width:20px;height:20px;border-radius:50%;background:rgba(255,255,255,.18);padding:0 4px}

  .hero{position:absolute;left:0;top:34px;width:100%;height:205px;
    background:linear-gradient(100deg,#8e8f92 0%,#6e7074 40%,#5d5a55 70%,#7d7a72 100%)}
  .hero-quote{position:absolute;left:18px;right:18px;top:64px;text-align:center;color:var(--white);
    font-family:"Rubik",sans-serif;font-weight:700;font-size:12px;line-height:1.5}
  .hero-quote .mark{font-size:22px;line-height:0;vertical-align:-6px}
  .btn{display:inline-flex;align-items:center;justify-content:center;background:var(--brand-red);color:var(--white);
    font-family:"Rubik",sans-serif;font-weight:500;border-radius:6px;box-shadow:0 3px 6px rgba(0,0,0,.2);white-space:nowrap}
  .hero .btn{position:absolute;left:149px;top:128px;width:72px;height:23px;font-size:7px}

  .intro-title{position:absolute;left:0;width:100%;top:272px;text-align:center;font-family:"Rubik",sans-serif;
    font-size:12.5px;color:var(--ink);font-weight:400;white-space:nowrap}
  .intro-title strong{color:var(--brand-red);font-weight:700}
  .intro-copy{position:absolute;left:20px;top:304px;width:214px;font-size:5.1px;line-height:1.95;color:var(--body-ink)}
  .intro-copy p+p{margin-top:9.5px}
  .intro-art{position:absolute;left:240px;top:351px;width:108px;height:128px;border-radius:6px;
    background:radial-gradient(circle at 50% 45%,#f1dcc4 0%,var(--cream) 70%)}
  .rule{position:absolute;left:20px;right:20px;top:510px;height:1px;background:var(--rule)}

  .services{position:absolute;left:0;top:512px;width:100%;height:128px}
  .services svg{position:absolute;left:0;top:0}
  .services-title{position:absolute;left:0;width:100%;top:28px;text-align:center;font-family:"Rubik",sans-serif;
    font-size:18px;color:var(--ink);font-weight:400}
  .services-title strong{color:var(--brand-red);font-weight:700}
  .services .btn{position:absolute;top:85px;width:92px;height:27px;font-size:6.5px;background:var(--deep-red);border-radius:8px}
  .services .btn:nth-of-type(1){left:70px}
  .services .btn:nth-of-type(2){left:213px}

  .nav-drawer{position:absolute;left:234px;top:34px;width:136px;height:214px;background:var(--menu-red);
    font-family:"Rubik",sans-serif;color:var(--white);box-shadow:0 4px 8px rgba(0,0,0,.2)}
  .nav-item{position:absolute;left:17px;right:17px;text-align:center;font-size:7px;line-height:8px;font-weight:500}
  .nav-divider{position:absolute;left:17px;right:17px;height:1px;background:rgba(255,255,255,.35)}
  .nav-sub{position:absolute;left:50px;top:102px;list-style:none;font-size:4.8px;font-weight:500;line-height:13.3px}
</style>
</head>
<body>

<section class="screen screen--compact" aria-label="Mobile home page">
  <header class="site-header">
    <div class="brand"><span class="brand-dot"></span>Orban Quill</div>
    <div class="site-title">Welcome To <strong>Orban Quill Pharmacovigilance</strong></div>
    <div class="menu-toggle"><span></span><span></span><span></span></div>
  </header>
  <div class="hero" role="img" aria-label="Photo of a pharmacist in a white coat holding a tablet in a pharmacy">
    <p class="hero-quote"><span class="mark">“</span>At Orban Quill we ensure that your business has the best Pharmacovigilance support in the industry.<span class="mark">”</span></p>
    <span class="btn">Learn More</span>
  </div>
  <h1 class="intro-title">Welcome To The <strong>Orban Quill Pharmacovigilance</strong> Website</h1>
  <div class="intro-copy">
    <p>We are an outsourcing partner to large and small companies within the pharmaceutical industry. Our range of services is tailored to suit each of our client’s needs and cover both human and veterinary medicinal products.</p>
    <p>Pharmacovigilance is defined by WHO as ‘The science and activities relating to the detection, assessment, understanding and prevention of adverse effects or any other drug-related problems’. The process is one of managing risk associated with medicinal products, in an effort to promote their safe and effective use by prescribers and patients.</p>
    <p>Our primary functions are EU QPPV and related pharmacovigilance services to assist and support Marketing Authorisation Holders (MAH), of pharmaceutical product licences, in their efforts to remain compliant with EU regulatory requirements (Regulation 1235/2010 and Directive 2010/84/EU) the deadline for which implementing ended on 21 July 2012.</p>
    <p>The regulatory environment is an ever-changing and evolving one. Legislation is global and the management of this process is complex, requiring a strong relationship between Marketing Authorisation Holders and their QPPV.</p>
  </div>
  <div class="intro-art" role="img" aria-label="Illustration of a medicine jar with a capsule"></div>
  <div class="rule"></div>
  <section class="services">
    <svg width="372" height="128" viewBox="0 0 372 128" aria-hidden="true"><path d="M0 30 C80 0 160 10 230 16 C300 22 340 12 372 4 L372 128 L0 128 Z" fill="#fdf1f1"/></svg>
    <h2 class="services-title">Our <strong>Medical Services</strong></h2>
    <span class="btn">Medical Information</span>
    <span class="btn">Pharmacovigilance</span>
  </section>
</section>

<section class="screen screen--menu-open" aria-label="Mobile home page with menu open">
  <header class="site-header">
    <div class="brand"><span class="brand-dot"></span>Orban Quill</div>
    <div class="site-title">Welcome To <strong>Orban Quill Pharmacovigilance</strong></div>
    <div class="menu-toggle"><span></span><span></span><span></span></div>
  </header>
  <div class="hero" role="img" aria-label="Photo of a pharmacist in a white coat holding a tablet in a pharmacy">
    <p class="hero-quote"><span class="mark">“</span>At Orban Quill we ensure that your business has the best Pharmacovigilance support in the industry.<span class="mark">”</span></p>
    <span class="btn">Learn More</span>
  </div>
  <h1 class="intro-title">Welcome To The <strong>Orban Quill Pharmacovigilance</strong> Website</h1>
  <div class="intro-copy">
    <p>We are an outsourcing partner to large and small companies within the pharmaceutical industry. Our range of services is tailored to suit each of our client’s needs and cover both human and veterinary medicinal products.</p>
    <p>Pharmacovigilance is defined by WHO as ‘The science and activities relating to the detection, assessment, understanding and prevention of adverse effects or any other drug-related problems’. The process is one of managing risk associated with medicinal products, in an effort to promote their safe and effective use by prescribers and patients.</p>
    <p>Our primary functions are EU QPPV and related pharmacovigilance services to assist and support Marketing Authorisation Holders (MAH), of pharmaceutical product licences, in their efforts to remain compliant with EU regulatory requirements (Regulation 1235/2010 and Directive 2010/84/EU) the deadline for which implementing ended on 21 July 2012.</p>
    <p>The regulatory environment is an ever-changing and evolving one. Legislation is global and the management of this process is complex, requiring a strong relationship between Marketing Authorisation Holders and their QPPV.</p>
  </div>
  <div class="intro-art" role="img" aria-label="Illustration of a medicine jar with a capsule"></div>
  <div class="rule"></div>
  <section class="services">
    <svg width="372" height="128" viewBox="0 0 372 128" aria-hidden="true"><path d="M0 30 C80 0 160 10 230 16 C300 22 340 12 372 4 L372 128 L0 128 Z" fill="#fdf1f1"/></svg>
    <h2 class="services-title">Our <strong>Medical Services</strong></h2>
    <span class="btn">Medical Information</span>
    <span class="btn">Pharmacovigilance</span>
  </section>

  <nav class="nav-drawer" aria-label="Main menu">
    <div class="nav-item" style="top:7px">Home</div>
    <div class="nav-divider" style="top:24px"></div>
    <div class="nav-item" style="top:35px">About Us</div>
    <div class="nav-divider" style="top:52px"></div>
    <div class="nav-item" style="top:62px;font-size:6px">QPPV</div>
    <div class="nav-divider" style="top:79px"></div>
    <div class="nav-item" style="top:89px">Our Services ⌃</div>
    <ul class="nav-sub">
      <li>Eudravigilance</li>
      <li>Pharmacovigilance</li>
      <li>Medical Information</li>
      <li>Literature Monitoring</li>
      <li>Medical Devices</li>
      <li>Training</li>
    </ul>
    <div class="nav-divider" style="top:189px"></div>
    <div class="nav-item" style="top:198px">Client</div>
  </nav>
</section>

</body>
</html>
```